Letterhead Design Project

Sunmark Growth Coaching Services

My info is
Daryna Feltwick-Osbourne
daryna@sunmarkgrowthco.com
sunmarkgrowthco.com
555-314-7720

you can play with order of items. I've never had a letterhead before. Thank you!

```html
<!DOCTYPE html>
<html lang="en">
<head>
<meta charset="utf-8">
<title>Sunmark Growth Coaching Services – Letterhead</title>
<link rel="stylesheet" href="https://fonts.googleapis.com/css2?family=Tinos:wght@400;700&display=swap">
<style>
  :root {
    --paper: #ffffff;
    --band-red: #c1213a;
    --band-orange: #f4901f;
    --band-yellow: #fde30c;
    --swash-tint: #c7cae6;
    --brand-red: #b81f35;
    --brand-orange: #ef8a1c;
    --ink: #111111;
  }
  html, body {
    margin: 0;
    padding: 0;
    overflow: hidden;
    background: var(--paper);
  }
  .letterhead {
    position: relative;
    width: 927px;
    height: 1200px;
    overflow: hidden;
    background: var(--paper);
    font-family: "Tinos", "Times New Roman", serif;
  }
  .letterhead__band,
  .letterhead__swash {
    position: absolute;
    inset: 0;
    width: 927px;
    height: 1200px;
  }
  .brand-dot { fill: var(--brand-orange); stroke: #ffffff; stroke-width: 4; }

  .brand {
    position: absolute;
    top: 124px;
    left: 585px;
    width: 300px;
    margin: 0;
    text-align: center;
    color: var(--brand-red);
    font-size: 33px;
    font-weight: 400;
    line-height: 1.05;
  }
  .contact {
    position: absolute;
    top: 214px;
    left: 582px;
    width: 300px;
    text-align: center;
    color: var(--ink);
    font-style: normal;
  }
  .contact__name {
    margin: 0 0 3px;
    font-size: 20px;
    font-weight: 700;
    line-height: 1.1;
  }
  .contact__line {
    margin: 0;
    font-size: 15.5px;
    font-weight: 400;
    line-height: 1.45;
  }
</style>
</head>
<body>
<main class="letterhead">
  <svg class="letterhead__swash" viewBox="0 0 927 1200" role="img" aria-label="Soft lavender swoosh ornament sweeping across the top of the page">
    <defs>
      <radialGradient id="swash-glow" cx="0.5" cy="0.5" r="0.5">
        <stop offset="0" stop-color="var(--swash-tint)" stop-opacity="0.55"/>
        <stop offset="1" stop-color="var(--swash-tint)" stop-opacity="0"/>
      </radialGradient>
    </defs>
    <ellipse cx="420" cy="230" rx="240" ry="250" fill="url(#swash-glow)"/>
  </svg>

  <svg class="letterhead__band" viewBox="0 0 927 1200" role="img" aria-label="Striped red, orange and yellow bands along the top and bottom edges">
    <defs>
      <linearGradient id="band-tones" x1="0" y1="0" x2="1" y2="0">
        <stop offset="0" stop-color="var(--band-red)"/>
        <stop offset="0.35" stop-color="var(--band-orange)"/>
        <stop offset="0.6" stop-color="var(--band-yellow)"/>
        <stop offset="1" stop-color="var(--band-red)"/>
      </linearGradient>
    </defs>
    <polygon points="0,0 927,0 927,54 0,141" fill="url(#band-tones)"/>
    <polygon points="0,1133 927,1088 927,1200 0,1200" fill="url(#band-tones)"/>
    <circle class="brand-dot" cx="735" cy="64" r="42"/>
  </svg>

  <p class="brand">Sunmark Growth<br>Coaching Services</p>

  <address class="contact">
    <p class="contact__name">Daryna Feltwick-Osbourne</p>
    <p class="contact__line">sunmarkgrowthco.com</p>
    <p class="contact__line">daryna@sunmarkgrowthco.com</p>
    <p class="contact__line">555-314-7720</p>
  </address>
</main>
</body>
</html>
```